Tervoni hd highway sign

would like a comercial truck in backround, and would like it very easy to read. Must have company name Tervoni H.D. Mechanical
would like address included 5142 larkfield frontage road. would a some bullet points on sign
-Commercial truck and trailer inspection and repair
-Heavy equipment repair
-24/7 Mobile service

```html
<!DOCTYPE html>
<html lang="en">
<head>
<meta charset="UTF-8">
<title>Tervoni H.D. Mechanical – Highway Sign</title>
<link rel="stylesheet" href="https://fonts.googleapis.com/css2?family=Saira+Condensed:wght@500;600&display=swap">
<style>
  :root {
    --stage: #e9edf1;
    --night-deep: #16132a;
    --night-mid: #2c2746;
    --night-soft: #4a4466;
    --teal: #4fbac2;
    --teal-bright: #5fd6dc;
    --white: #ffffff;
    --ink: #1d1d24;
    --dot-rim: #d9dde2;
  }
  * { box-sizing: border-box; margin: 0; padding: 0; }
  html, body {
    width: 1200px; height: 720px; overflow: hidden;
    background: var(--stage);
    font-family: "Saira Condensed", "Arial Narrow", sans-serif;
  }
  .sign {
    position: absolute; left: 30px; top: 120px;
    width: 1140px; height: 480px; overflow: hidden;
    background: linear-gradient(180deg, var(--night-soft) 0%, var(--night-mid) 35%, var(--night-deep) 100%);
  }
  .truck-photo {
    position: absolute; left: 250px; top: 40px; width: 560px; height: 340px;
    background:
      radial-gradient(ellipse at 45% 45%, rgba(79,186,194,0.55) 0%, rgba(79,186,194,0.18) 40%, rgba(22,19,42,0) 70%),
      radial-gradient(ellipse at 50% 85%, rgba(160,165,190,0.35) 0%, rgba(22,19,42,0) 60%);
  }
  .road-glow {
    position: absolute; left: 0; top: 270px; width: 1140px; height: 90px;
    background: linear-gradient(180deg, rgba(22,19,42,0) 0%, rgba(150,150,175,0.28) 50%, rgba(22,19,42,0) 100%);
  }
  .company-name, .address {
    position: absolute; color: var(--white); font-weight: 500;
    letter-spacing: 0.5px; text-transform: uppercase; line-height: 1;
  }
  .company-name { left: 58px; top: 48px; font-size: 34px; }
  .address { right: 70px; top: 26px; font-size: 40px; }
  .rule {
    position: absolute; height: 6px; background: var(--teal);
  }
  .rule--name { left: 140px; top: 100px; width: 150px; }
  .rule--address { right: 175px; top: 84px; width: 190px; }
  .services { position: absolute; inset: 0; }
  .service-label {
    position: absolute; width: 150px; text-align: center;
    color: var(--ink); font-weight: 500; font-size: 19px; line-height: 1.05;
    text-transform: uppercase;
  }
</style>
</head>
<body>
  <section class="sign">
    <div class="truck-photo" role="img" aria-label="Commercial semi truck cab outlined in glowing teal light on a dark night road"></div>
    <div class="road-glow"></div>

    <h1 class="company-name">Tervoni H.D. Mechanical</h1>
    <div class="rule rule--name"></div>
    <p class="address">5142 Larkfield Frontage Road</p>
    <div class="rule rule--address"></div>

    <svg class="services" viewBox="0 0 1140 480" width="1140" height="480" aria-hidden="true">
      <ellipse class="hill" cx="541" cy="540" rx="405" ry="270" fill="var(--teal)" stroke="var(--white)" stroke-width="4"/>
      <g class="hill-dots" fill="var(--white)" stroke="var(--dot-rim)" stroke-width="4">
        <circle cx="185" cy="412" r="13"/>
        <circle cx="405" cy="286" r="13"/>
        <circle cx="662" cy="282" r="13"/>
        <circle cx="902" cy="410" r="13"/>
      </g>
      <g class="hex" transform="translate(290 378)">
        <polygon points="0,-105 91,-52 91,52 0,105 -91,52 -91,-52" fill="var(--white)" stroke="var(--teal)" stroke-width="8"/>
        <circle cy="-52" r="20" fill="var(--teal)"/>
        <path d="M-9 -52 l6 6 l12 -12" fill="none" stroke="var(--white)" stroke-width="4" stroke-linecap="round" stroke-linejoin="round"/>
      </g>
      <g class="hex" transform="translate(540 350)">
        <polygon points="0,-105 91,-52 91,52 0,105 -91,52 -91,-52" fill="var(--white)" stroke="var(--teal)" stroke-width="8"/>
        <circle cy="-52" r="20" fill="var(--teal)"/>
        <path d="M-9 -52 l6 6 l12 -12" fill="none" stroke="var(--white)" stroke-width="4" stroke-linecap="round" stroke-linejoin="round"/>
      </g>
      <g class="hex" transform="translate(790 340)">
        <polygon points="0,-105 91,-52 91,52 0,105 -91,52 -91,-52" fill="var(--white)" stroke="var(--teal)" stroke-width="8"/>
        <circle cy="-52" r="20" fill="var(--teal)"/>
        <path d="M-9 -52 l6 6 l12 -12" fill="none" stroke="var(--white)" stroke-width="4" stroke-linecap="round" stroke-linejoin="round"/>
      </g>
    </svg>

    <p class="service-label" style="left:215px; top:350px;">Commercial truck and trailer inspection and repair</p>
    <p class="service-label" style="left:465px; top:330px;">Heavy equipment repair</p>
    <p class="service-label" style="left:715px; top:320px;">24/7 mobile service</p>
  </section>
</body>
</html>
```